Home page redesign for an international job board

Need a modern design based on current structure of the page. I am happy with the current structure and layout/architecture, not entirely happy with how it looks. While I still want to keep most of the elements in place ( especially the search box) I would like to get another look and feel - more appealing to any audience related to online job search

Home page is: www.lucrubrisa.ro

Target Market(s)

job seeekers and employers

Industry/Entity Type

Architecture

Number of Pages Required

1 page

Font styles to use
Sans Serif

Colors
33a6d7

Requirements
Must have
• Stay with the same structure: Seach box, latest jobs, articles
Nice to have
• Key element: search for jobs - this needs to be very clear

```html
<!DOCTYPE html>
<html lang="en">
<head>
<meta charset="utf-8">
<title>LucruBrisa – Job Search</title>
<link href="https://fonts.googleapis.com/css2?family=Raleway:wght@400;500;600&family=Open+Sans:wght@400;600&display=swap" rel="stylesheet">
<style>
:root{
  --blue:#33a6d7;
  --blue-dark:#1f86bd;
  --navy:#0f5f86;
  --red:#d71f26;
  --ink:#333;
  --grey:#888;
  --line:#dcdcdc;
}
*{box-sizing:border-box;margin:0;padding:0}
html,body{width:800px;height:1200px;overflow:hidden;background:#fff}
body{position:relative;font-family:"Open Sans",sans-serif;color:var(--ink)}
.abs{position:absolute}

.top-links{left:516px;top:8px;font-size:7.5px;color:#777;word-spacing:1px}
.brand{left:104px;top:28px;display:flex;align-items:center;gap:6px}
.brand-dot{width:32px;height:32px;border-radius:50%;background:var(--red)}
.brand-name{font-family:"Raleway",sans-serif;font-weight:600;font-size:17px;color:#333}
.btn{display:block;color:#fff;font-size:8px;text-align:center;line-height:20px}
.btn-login{left:587px;top:44px;width:51px;height:20px;background:var(--navy)}
.btn-register{left:643px;top:44px;width:53px;height:20px;background:var(--red)}

.nav{left:0;top:76px;width:800px;height:34px;background:linear-gradient(#3fb0df,#2c9bcf)}
.nav ul{list-style:none;display:flex;margin-left:98px;height:34px}
.nav li{font-family:"Raleway",sans-serif;color:#fff;font-size:12px;line-height:34px;padding:0 19px}
.nav li.active{background:var(--blue-dark);padding:0 21px}

.hero{left:0;top:110px;width:800px;height:300px;background:linear-gradient(100deg,#8e9aa6 0%,#c9d0d6 35%,#e2e4e4 55%,#6d7580 100%)}
.search-box{left:210px;top:184px;width:387px;height:132px;background:rgba(120,125,130,.55);border:1px solid rgba(255,255,255,.45)}
.search-title{left:210px;top:194px;width:387px;text-align:center;color:#fff;font-family:"Raleway",sans-serif;font-size:17px}
.field{background:#fff;border:1px solid #ccc;height:22px;font-size:7.5px;color:#777;line-height:20px;padding-left:9px}
.field svg{position:absolute;right:8px;top:7px}
.btn-search{left:501px;top:276px;width:79px;height:22px;background:var(--blue);color:#fff;font-size:10px;text-align:center;line-height:22px}
.dots{left:371px;top:389px;display:flex;gap:4px}
.dots i{width:11px;height:11px;border-radius:50%;background:#fff}
.dots i:first-child{background:var(--blue)}

.features{left:105px;top:427px;width:590px;height:117px;border:1px solid var(--line);background:linear-gradient(#fff 55%,#eeeeee);display:flex}
.feature{position:relative;border-right:1px solid var(--line);flex:none}
.feature:nth-child(1){width:192px}
.feature:nth-child(2){width:193px}
.feature:nth-child(3){width:203px;border-right:none}
.feature-icon{position:absolute;left:11px;top:17px;width:47px;height:47px;border-radius:50%;background:var(--blue)}
.feature:nth-child(3) .feature-icon{left:8px}
.feature-icon svg{position:absolute;left:12px;top:12px}
.feature h3{position:absolute;left:68px;top:17px;font-family:"Raleway",sans-serif;font-weight:400;font-size:13px;color:var(--blue);white-space:nowrap}
.feature p{position:absolute;left:69px;top:40px;width:118px;font-size:6.5px;line-height:12px;color:#888}
.btn-more{position:absolute;left:69px;top:79px;width:59px;height:18px;background:var(--navy);color:#fff;font-size:7.5px;text-align:center;line-height:18px}
.feature:nth-child(3) h3{left:60px;font-size:12.5px}
.feature:nth-child(3) p,.feature:nth-child(3) .btn-more{left:61px}

.articles-title{left:105px;top:587px;font-family:"Raleway",sans-serif;font-weight:400;font-size:16px;color:#333}
.article-img{width:117px;height:78px;border:1px solid var(--line)}
.article{width:250px}
.article h4{font-family:"Raleway",sans-serif;font-weight:500;font-size:10.5px;color:var(--blue)}
.article p{font-size:6.5px;line-height:12px;color:#888;margin-top:3px}
.article .read{font-size:7px;color:var(--navy);font-weight:600;margin-top:4px}
.article .date{font-size:6px;color:#555;margin-top:6px}

.apps{left:504px;top:590px;width:187px;height:209px;border:1px solid var(--line)}
.app{position:relative;height:69.6px;border-bottom:1px solid var(--line);background:linear-gradient(#fff 50%,#f0f0f0)}
.app:last-child{border-bottom:none}
.app h5{position:absolute;left:14px;top:12px;font-family:"Raleway",sans-serif;font-weight:500;font-size:10px;color:var(--navy);white-space:nowrap}
.app p{position:absolute;left:14px;top:31px;font-size:6.5px;color:#888}
.app .btn-small{position:absolute;left:16px;top:46px;width:47px;height:15px;background:var(--blue);color:#fff;font-size:6.5px;text-align:center;line-height:15px}
.app .art{position:absolute;right:6px;top:5px;width:40px;height:60px;border-radius:6px;background:linear-gradient(#cfe9f5,#9fcfe5)}

.banner{left:0;top:848px;width:800px;height:172px;background:linear-gradient(90deg,#4a5158,#6f767d 45%,#59606a)}
.banner h2{position:absolute;left:0;top:40px;width:800px;text-align:center;font-family:"Raleway",sans-serif;font-weight:400;font-size:19px;line-height:23px;color:#fff}
.banner p{position:absolute;left:130px;top:94px;width:540px;text-align:center;font-size:9px;line-height:15px;color:#fff}

.footer{left:0;top:1020px;width:800px;height:180px;background:linear-gradient(#4ab2e0,#2e98cf)}
.fcol{position:absolute;top:22px;color:#fff}
.fcol h6{font-family:"Raleway",sans-serif;font-weight:500;font-size:11.5px;margin-bottom:6px}
.fcol li{list-style:none;font-size:7px;line-height:13.5px}
.social{display:flex;gap:6px;margin-top:8px}
.social i{width:11px;height:11px;border-radius:50%;background:#fff}
.partner-badge{left:579px;top:1065px;width:93px;height:68px;border-radius:50%;background:#fff}
.footer-rule{left:0;top:1159px;width:800px;height:1px;background:rgba(255,255,255,.3)}
.copyright{left:104px;top:1174px;font-size:7px;color:#d8eef8}
</style>
</head>
<body>

<div class="abs top-links">Jobs &nbsp;|&nbsp; Career Coach &nbsp;|&nbsp; Interview Tips &nbsp;|&nbsp; Ro &nbsp;|&nbsp; En</div>
<div class="abs brand"><span class="brand-dot"></span><span class="brand-name">LucruBrisa</span></div>
<a class="abs btn btn-login">LOGIN</a>
<a class="abs btn btn-register">REGISTER</a>

<nav class="abs nav">
  <ul>
    <li class="active">Search Jobs</li>
    <li>My Account</li>
    <li>Career Counselling</li>
    <li>Features</li>
    <li>Employer &amp; Post a Job</li>
  </ul>
</nav>

<div class="abs hero" role="img" aria-label="Photo of smiling business people shaking hands in an office"></div>
<div class="abs search-box"></div>
<div class="abs search-title">Search Your Dream Job Here</div>
<div class="abs field" style="left:227px;top:224px;width:351px">Type Keyword</div>
<div class="abs field" style="left:227px;top:250px;width:171px">Choose Category<svg width="9" height="6"><path d="M1 1l3.5 3.5L8 1" fill="none" stroke="#999"/></svg></div>
<div class="abs field" style="left:405px;top:248px;width:173px">Select Region<svg width="9" height="6"><path d="M1 1l3.5 3.5L8 1" fill="none" stroke="#999"/></svg></div>
<div class="abs field" style="left:227px;top:276px;width:132px">Work Type<svg width="9" height="6"><path d="M1 1l3.5 3.5L8 1" fill="none" stroke="#999"/></svg></div>
<div class="abs field" style="left:363px;top:276px;width:134px">Select Location<svg width="9" height="6"><path d="M1 1l3.5 3.5L8 1" fill="none" stroke="#999"/></svg></div>
<div class="abs btn-search">Search</div>
<div class="abs dots"><i></i><i></i><i></i><i></i></div>

<section class="abs features">
  <div class="feature">
    <div class="feature-icon"><svg width="23" height="23" fill="none" stroke="#fff" stroke-width="1.4"><rect x="4" y="2" width="15" height="19"/><path d="M7 7h9M7 11h9M7 15h6"/></svg></div>
    <h3>Post Your Resume</h3>
    <p>Suspendisse quam leo molestie sed luctus quis feugiat in pede Fusce tellus Sed metus augue</p>
    <span class="btn-more">Click here</span>
  </div>
  <div class="feature">
    <div class="feature-icon"><svg width="23" height="23" fill="none" stroke="#fff" stroke-width="1.4"><path d="M5 17V11a6.5 6.5 0 0113 0v6l2 2H3z"/><path d="M9.5 21a2 2 0 004 0"/></svg></div>
    <h3>Set your Job Alert</h3>
    <p>Suspendisse quam leo molestie sed luctus quis feugiat in pede Fusce tellus Sed metus augue</p>
    <span class="btn-more">Click here</span>
  </div>
  <div class="feature">
    <div class="feature-icon"><svg width="23" height="23" fill="none" stroke="#fff" stroke-width="1.4"><rect x="4" y="2" width="15" height="19"/><circle cx="10" cy="10" r="4"/><path d="M13 13l5 5"/></svg></div>
    <h3>Manage your Job search</h3>
    <p>Suspendisse quam leo molestie sed luctus quis feugiat in pede Fusce tellus Sed metus augue</p>
    <span class="btn-more">Click here</span>
  </div>
</section>

<h2 class="abs articles-title">Latest Articles</h2>
<div class="abs article-img" style="left:105px;top:619px;background:linear-gradient(135deg,#b9bec4,#5d646c)" role="img" aria-label="Photo of a hand pointing at a group of people icons"></div>
<article class="abs article" style="left:232px;top:618px">
  <h4>Invatarea, continua pe tot parcursul vietii</h4>
  <p>Suspendisse quam leo molestie sed luctus quis feugiat in pede Fusce tellus Sed metus augue convallis et vehicula ut pulvinar eu ante Integer orci tellus tristique vitae consequat nec</p>
  <div class="read">Read More</div>
  <div class="date">Posted on 14 Nov 2015</div>
</article>
<div class="abs article-img" style="left:105px;top:725px;background:linear-gradient(135deg,#a8c6de,#e0dad2)" role="img" aria-label="Photo of two young people studying at a laptop"></div>
<article class="abs article" style="left:232px;top:724px">
  <h4>Invatarea, continua pe tot parcursul vietii</h4>
  <p>Suspendisse quam leo molestie sed luctus quis feugiat in pede Fusce tellus Sed metus augue convallis et vehicula ut pulvinar eu ante Integer orci tellus tristique vitae consequat nec</p>
  <div class="read">Read More</div>
  <div class="date">Posted on 14 Nov 2015</div>
</article>

<aside class="abs apps">
  <div class="app"><h5>Job app for Orbit phone</h5><p>Ellus Sed metus augue convallis et</p><span class="btn-small">Read More</span><div class="art" role="img" aria-label="Hand holding a smartphone"></div></div>
  <div class="app"><h5>Job app for Robo OS</h5><p>Ellus Sed metus augue conval</p><span class="btn-small">Read More</span><div class="art" style="background:linear-gradient(#d6ecb0,#8fc04a)" role="img" aria-label="Green robot mascot illustration"></div></div>
  <div class="app"><h5>Job app for Friendnet</h5><p>Ellus Sed metus augue convallis et</p><span class="btn-small">Read More</span><div class="art" role="img" aria-label="Hand holding a phone showing a social app"></div></div>
</aside>

<section class="abs banner" role="img" aria-label="Dimmed photo of people reviewing documents at a desk">
  <h2>International careers. Overseas jobs and<br>employment opportunities</h2>
  <p>LucruBrisa.ro is a job search and employment resource.For jobseekers we provide jobs from Romanian and International employers and for hiring managers we aim to deliver quality candidates across all fields of expertise.</p>
</section>

<footer class="abs footer">
  <div class="fcol" style="left:106px"><h6>Go Mobile</h6><ul><li>Orbit phone App</li><li>Robo OS App</li><li>Friendnet App</li><li>Mobile Version</li></ul></div>
  <div class="fcol" style="left:202px"><h6>Employer Tools</h6><ul><li>Post job ads</li><li>Access</li><li>jobseekers</li><li>Resume Search</li><li>Analytics</li></ul></div>
  <div class="fcol" style="left:319px;top:20px"><h6>Job Seeker Tools</h6><ul><li>Resume Posting</li><li>Job Alerts</li><li>Video Resume</li><li>Create Profile</li></ul></div>
  <div class="fcol" style="left:456px"><h6>Get in touch</h6><ul><li>Pleae connect with us on</li></ul><div class="social"><i></i><i></i><i></i><i></i></div></div>
  <div class="fcol" style="left:585px"><h6>Our Partners</h6></div>
</footer>
<div class="abs partner-badge"></div>
<div class="abs footer-rule"></div>
<div class="abs copyright">© 2015 Company Name &nbsp;All right reserved &nbsp;Term of Use</div>

</body>
</html>
```